Cruise & Resort Travel Redemption Vouchers

Need to have all of these pages completely re-done. These designs are horrible and need to look much more professional. The individual vouchers like the "silver gull laugh house" & Crimson lantern feast can look similar to the design on their websites.
New york link
http://gulllaughsfl.com/
Crimson Lantern Feast
http://www.crimson-lantern.com/
Please do something with the tiny anchors all over the place. Or just get rid of them.
Does not need to be over the top design heavy...just professional and simple with small doses of vacation added.
Updates
get rid of the stupid anchors all over the place.
Target Market(s)
35-60
Industry/Entity Type
Club
Requirements
Must have
- All pages done.
The company logo on the pages,found here.
http://harborgetawayoffers.com/
The Abbreviation is R.T.B

```html
<!DOCTYPE html>
<html lang="en">
<head>
<meta charset="utf-8">
<title>The Harbor Getaway Store – Vacation of a Lifetime Destinations</title>
<link href="https://fonts.googleapis.com/css2?family=Arimo:ital,wght@0,400;0,700;1,700&display=swap" rel="stylesheet">
<style>
  :root {
    --navy: #2b3990;
    --cyan: #00aeef;
    --cyan-soft: #9fdcf5;
    --ink: #1c1c1c;
    --rule: #5b4f9c;
    --paper: #ffffff;
  }
  * { margin: 0; padding: 0; box-sizing: border-box; }
  html, body { width: 943px; height: 1200px; overflow: hidden; background: var(--paper); }
  body { font-family: "Arimo", Arial, sans-serif; color: var(--ink); }

  .sheet { position: relative; width: 943px; height: 1200px; overflow: hidden;
    background: linear-gradient(90deg, var(--cyan) 0%, #ffffff 14%, #ffffff 86%, var(--cyan) 100%); }

  .masthead { position: absolute; left: 0; top: 0; width: 943px; height: 196px; background: var(--paper);
    border-bottom: 2px solid var(--rule); }
  .brand { position: absolute; left: 52px; top: 92px; display: flex; align-items: center; gap: 10px;
    font-weight: 700; font-size: 19px; color: var(--navy); }
  .brand-dot { width: 16px; height: 16px; border-radius: 50%; background: var(--navy); }
  .store-name { position: absolute; left: 330px; width: 520px; top: 90px; text-align: center;
    font-weight: 700; font-size: 22px; color: var(--navy); letter-spacing: .3px; }
  .headline { position: absolute; left: 330px; width: 560px; top: 122px; text-align: center;
    font-weight: 700; font-style: italic; font-size: 31px; color: var(--navy); letter-spacing: -.3px; }

  .col-east { position: absolute; left: 0; top: 196px; width: 468px; height: 954px;
    background: linear-gradient(90deg, var(--cyan) 0%, #ffffff 15%, #ffffff 78%, var(--cyan) 100%);
    border-right: 2px solid var(--rule); border-bottom: 2px solid var(--rule); }
  .col-right { position: absolute; left: 470px; top: 196px; width: 473px; height: 1004px;
    background: linear-gradient(90deg, #ffffff 0%, #ffffff 62%, var(--cyan) 100%); }

  .region-bar { position: absolute; height: 22px; font-weight: 700; font-size: 15px; line-height: 22px;
    padding-left: 14px; color: var(--ink); }
  .col-east .region-bar { left: 140px; width: 300px; top: 5px;
    background: linear-gradient(90deg, var(--cyan-soft), #e8f7fd 70%, rgba(255,255,255,0)); }
  .col-right .region-bar { left: 0; width: 473px; border-top: 2px solid #d7d7d7;
    background: linear-gradient(90deg, #ffffff 0%, var(--cyan-soft) 40%, var(--cyan) 100%); padding-left: 40px; }

  .place-list { position: absolute; list-style: none; font-size: 13.5px; }
  .col-east .place-list { left: 154px; top: 35px; line-height: 18.3px; }
  .col-right .place-list { left: 40px; }
  .place-list.paired li { display: grid; grid-template-columns: 128px auto; }

  .closing-rule { position: absolute; left: 0; top: 888px; width: 473px; height: 2px; background: var(--rule); }
  .disclaimer { position: absolute; left: 20px; width: 433px; top: 908px; text-align: center;
    font-weight: 700; font-style: italic; font-size: 13.5px; line-height: 20px; }
</style>
</head>
<body>
<div class="sheet">
  <header class="masthead">
    <div class="brand"><span class="brand-dot"></span>The Harbor Getaway Store</div>
    <div class="store-name">THE HARBOR GETAWAY STORE</div>
    <h1 class="headline">VACATION OF &nbsp;A LIFETIME DESTINATIONS</h1>
  </header>

  <section class="col-east">
    <h2 class="region-bar">NORTH AMERICA &nbsp;-EAST</h2>
    <ul class="place-list">
      <li>Collinwood, CAN</li><li>Atlantic Beach, NC</li><li>Banner Elk, NC</li><li>Brunswick, GA</li>
      <li>Cape Cod/Falmouth, MA</li><li>Charleston, SC</li><li>Cocoa Beach, FL</li><li>Daytona Beach, FL</li>
      <li>Ft. Lauderdale, FL</li><li>St. Augustine, FL</li><li>St. Simons, GA</li><li>Virginia Beach, VA</li>
      <li>Williamsburg, VA</li><li>Portland, ME</li><li>Gordonsville, VA</li><li>Hilton Head, SC</li>
      <li>Lincoln, NH</li><li>Miami, FL</li><li>Merrells Inlet, CS</li><li>Myrtle Beach, SC</li>
      <li>Naples, FL</li><li>Orlando, FL</li><li>New Smyrna Beach, FL</li><li>Pigeon Forge, TN</li>
      <li>Collinwood, CAN</li><li>Atlantic BEach, NC</li><li>Banner Elk, NC</li><li>Brunswick, GA</li>
      <li>Cape Cod/Falmouth, MA</li><li>Charleston, SC</li><li>Cocoa BEach, FL</li><li>Daytona Beach, FL</li>
      <li>Ft. Lauderdale, FL</li><li>St. Augustine, FL</li><li>St. Simons, GA</li><li>Virginia Beach, VA</li>
      <li>Williamsburg, VA</li><li>Portland, ME</li><li>Gordonsville, VA</li><li>Hilton Head, SC</li>
      <li>Lincoln, NH</li><li>Miami, FL</li><li>Murrells Inlet, SC</li><li>Myrtle BEach, SC</li>
      <li>Naples, FL</li><li>ORlando, FL</li><li>New Smyrna Beach, FL</li><li>Pigeon Forge, TN</li>
      <li>Gatlinburg, TN</li>
    </ul>
  </section>

  <section class="col-right">
    <h2 class="region-bar" style="top:4px">NORT AMERICA - CENTRAL</h2>
    <ul class="place-list" style="top:40px; line-height:21px">
      <li>New Ul, TX</li><li>New Orleans, LA</li><li>Biloxi, MS</li><li>Branson, MO</li><li>Dallas, TX</li>
    </ul>

    <h2 class="region-bar" style="top:181px">NORT AMERICA - WEST</h2>
    <ul class="place-list" style="top:214px; line-height:19.3px">
      <li>Park City, UT</li><li>Kent, WA</li><li>Lake Havasu, AZ</li><li>Lake Tahoe, CA</li>
      <li>Las Vegas, NV</li><li>San Antonio, TX</li><li>San Diego, CA</li><li>Scottsdale, AZ</li>
      <li>Sedona, AZ</li><li>GEnoa, NV</li>
    </ul>

    <h2 class="region-bar" style="top:444px">MEXICO</h2>
    <ul class="place-list paired" style="top:474px; line-height:21px">
      <li><span>Puerto Vallarta</span><span>Mexico</span></li>
      <li><span>Cabo San Lucas</span><span>Mexico</span></li>
      <li><span>Cozumel</span><span>Mexico</span></li>
      <li><span>Cancun</span><span>Mexico</span></li>
      <li><span>Playacar</span><span>Mexico</span></li>
    </ul>

    <h2 class="region-bar" style="top:622px">THE CARIBBEAN</h2>
    <ul class="place-list paired" style="top:654px; line-height:21.5px">
      <li><span>Freeport</span><span>Bahamas</span></li>
      <li><span>Guanacaste</span><span>Costa Rica</span></li>
      <li><span>Grand Cayman</span><span>Cayman Islands</span></li>
      <li><span>Punta Cana</span><span>Dominican Republic</span></li>
    </ul>

    <h2 class="region-bar" style="top:776px">ABROAD</h2>
    <ul class="place-list paired" style="top:812px; line-height:21px">
      <li><span>Koh Samui</span><span>Thailand</span></li>
      <li><span>Pattaya</span><span>Thailand</span></li>
      <li><span>Phuket</span><span>Thailand</span></li>
    </ul>

    <div class="closing-rule"></div>
    <p class="disclaimer">We reserve the right to add or remove destinations, at any time, based on availability and allotments</p>
  </section>
</div>
</body>
</html>
```